We are growing our coaching practice and need some help creating collateral

Our organisation is building a coaching practice. It's going well and we want to take it to the next level. To date, we've done our own basic marketing material (attached), but now we want to create something more substantial that captures our approach and gives us confidence and pride when talking to customers. Things to note - we aren't looking for logo design, that's a separate branding discussion in our organisation. We are looking for someone to take our existing content and make it look good - this might be in the form of a flyer or PPT slide deck for example.
The format we are looking for is the offering title - in this case, 'Coaching', a brief description, and then some further detail.
Target Market(s)
Corporate, Healthcare, IT
Colors
Designer to choose colors to be used in the design.
Look and feel
Each slider illustrates characteristics of the customer's brand and the style your logo design should communicate.

```html
<!DOCTYPE html>
<html lang="en">
<head>
<meta charset="utf-8">
<title>NWC Executive Coaching Flyer</title>
<link rel="stylesheet" href="https://fonts.googleapis.com/css2?family=Montserrat:wght@600;700&family=Lato:ital,wght@0,300;0,400;0,700;1,400&display=swap">
<style>
  :root {
    --backdrop: #ecebea;
    --paper: #ffffff;
    --accent: #e0613f;
    --navy: #2e3142;
    --ink: #1f2027;
    --body: #6a6a6f;
    --rule: #e6e6e6;
    --photo-light: #d9d9d9;
    --photo-dark: #6d6d6d;
  }
  * { box-sizing: border-box; margin: 0; padding: 0; }
  html, body { width: 1200px; height: 819px; overflow: hidden; }
  body { background: var(--backdrop); font-family: "Lato", Arial, sans-serif; position: relative; }

  .flyer {
    position: absolute; left: 320px; top: 15px;
    width: 559px; height: 788px;
    background: var(--paper);
    box-shadow: 0 2px 10px rgba(0,0,0,0.12);
    overflow: hidden;
  }

  .brand {
    position: absolute; left: 33px; top: 26px;
    display: flex; align-items: center; gap: 7px;
    font-family: "Lato", Arial, sans-serif; font-weight: 300;
    font-size: 25px; letter-spacing: 0.5px; color: var(--navy);
  }
  .brand-dot { width: 9px; height: 9px; border-radius: 50%; background: var(--accent); }

  .site-link {
    position: absolute; right: 44px; top: 38px;
    font-size: 9px; font-weight: 700; color: var(--ink);
  }

  .hero-photo {
    position: absolute; left: 0; top: 76px; width: 235px; height: 290px;
    background: linear-gradient(120deg, var(--photo-light) 0%, #a9a9a9 55%, var(--photo-dark) 100%);
  }
  .hero-panel {
    position: absolute; left: 235px; top: 76px; width: 324px; height: 290px;
    background: var(--accent); color: var(--paper); text-align: right;
    padding: 70px 44px 0 20px;
  }
  .hero-title {
    font-family: "Montserrat", Arial, sans-serif; font-weight: 700;
    font-size: 21px; line-height: 1.3;
  }
  .hero-lead { margin-top: 26px; font-size: 12.4px; line-height: 1.42; }
  .hero-lead strong { font-weight: 700; }

  .pillar-icon {
    position: absolute; top: 338px; width: 56px; height: 56px; border-radius: 50%;
    background: var(--navy); display: flex; align-items: center; justify-content: center;
  }
  .pillar { position: absolute; top: 415px; width: 142px; }
  .pillar h2, .packages h2 {
    font-family: "Montserrat", Arial, sans-serif; font-weight: 700;
    font-size: 13.5px; color: var(--ink);
  }
  .pillar p {
    margin-top: 14px; font-size: 8.6px; line-height: 1.38; color: var(--body);
  }

  .packages { position: absolute; left: 39px; top: 571px; width: 315px; }
  .packages p { margin-top: 12px; font-size: 8.6px; line-height: 1.38; color: var(--body); }
  .packages .invite { margin-top: 10px; color: var(--accent); font-size: 7.8px; }

  .contact-bar {
    position: absolute; left: 39px; top: 700px; width: 279px; height: 26px;
    display: flex; font-size: 8.6px;
  }
  .contact-label {
    width: 62px; background: var(--navy); color: var(--paper);
    padding: 3px 6px; line-height: 1.15;
  }
  .contact-label strong { font-weight: 700; }
  .contact-details {
    flex: 1; background: var(--accent); color: var(--ink);
    display: flex; align-items: center; gap: 5px; padding-left: 6px;
  }
  .contact-details svg { flex: none; }

  .detail-photo {
    position: absolute; left: 370px; top: 572px; width: 189px; height: 153px;
    border-left: 4px solid var(--accent);
    background: linear-gradient(150deg, #f0f0f0 0%, #bdbdbd 50%, #7c7c7c 100%);
  }

  .footer-rule { position: absolute; left: 0; top: 755px; width: 221px; height: 4px; background: var(--rule); }
  .footer-note {
    position: absolute; right: 44px; top: 750px;
    font-size: 8.8px; font-weight: 700; color: var(--ink);
  }
</style>
</head>
<body>
  <main class="flyer">
    <div class="brand"><span>northway</span><span class="brand-dot"></span></div>
    <div class="site-link">www.northwaycoaching.com</div>

    <div class="hero-photo" role="img" aria-label="Black and white photo of a smiling coach gesturing in a bright office meeting"></div>
    <section class="hero-panel">
      <h1 class="hero-title">NWC Executive<br>Coaching</h1>
      <p class="hero-lead"><strong>We believe great coaching is a bridge:</strong> one that enables you to see more clearly and cross the unexpected chasms; one that supports and challenges your thinking and actions to progress your significant goals.</p>
    </section>

    <div class="pillar-icon" style="left:40px">
      <svg width="22" height="26" viewBox="0 0 22 26" fill="none" stroke="#fff" stroke-width="2">
        <path d="M11 2a8 8 0 0 0-5 14.2c1 .9 1.5 2 1.5 3.3h7c0-1.3.5-2.4 1.5-3.3A8 8 0 0 0 11 2z"/>
        <path d="M8 22.5h6M9 25h4"/>
      </svg>
    </div>
    <div class="pillar-icon" style="left:207px">
      <svg width="30" height="20" viewBox="0 0 30 20" fill="#fff">
        <circle cx="15" cy="5" r="4"/><path d="M8 18c0-4 3-7 7-7s7 3 7 7z"/>
        <circle cx="6" cy="7" r="3"/><path d="M0 18c0-3 2.5-5.5 6-5.5 1 0 2 .2 2.6.6C7.5 14.5 7 16 7 18z"/>
        <circle cx="24" cy="7" r="3"/><path d="M30 18c0-3-2.5-5.5-6-5.5-1 0-2 .2-2.6.6 1.1 1.4 1.6 2.9 1.6 4.9z"/>
      </svg>
    </div>
    <div class="pillar-icon" style="left:374px">
      <svg width="26" height="26" viewBox="0 0 26 26" fill="#fff">
        <polygon points="13,0 16,4 21,3 21,8 26,11 23,14 26,18 21,19 20,24 15,22 13,26 11,22 6,24 5,19 0,18 3,14 0,11 5,8 5,3 10,4"/>
      </svg>
    </div>

    <section class="pillar" style="left:39px">
      <h2>Partnership</h2>
      <p>We build a creative and confidential partnership with you, one that is grounded in the science of leadership, change and coaching psychology so that practical results are an expectation and not left to chance.</p>
    </section>
    <section class="pillar" style="left:207px">
      <h2>Our Coaches</h2>
      <p>Our coaches are highly attuned to the human systems within which you work and live, since understanding those interconnected forces is vital to unlock movement. We build on your existing strengths and seek sustainable shifts, ones that create ripple effects of positive change.</p>
    </section>
    <section class="pillar" style="left:374px">
      <h2>Become a Leader</h2>
      <p>Leaders everywhere face unprecedented change, pressure, ambiguity, culture and accountability dilemmas. And yet every leader also has a different story, different terrain to navigate and different aspirations. This is where executive coaching with NWC can create extraordinary results.</p>
    </section>

    <section class="packages">
      <h2>Our Packages</h2>
      <p>Our coaching packages typically consist of blocks of 7 hourly sessions, conducted fortnightly (with flexibility to customise).<br>For EL2 leaders, the investment in a block of 7 sessions is $3400 + GST. This includes significant preparation and conceptualisation time before and after sessions by your coach to ensure you achieve maximum value.</p>
      <p class="invite">Why not explore the possibilities executive coaching offers through a no obligation initial session, ensuring the approach and the coach is a good fit for you?</p>
    </section>

    <div class="contact-bar">
      <div class="contact-label">Contact<br><strong>Dana Mercer</strong></div>
      <div class="contact-details">
        <svg width="10" height="8" viewBox="0 0 10 8"><rect width="10" height="8" fill="#fff"/><path d="M0 0l5 4 5-4" fill="none" stroke="#2e3142" stroke-width="1"/></svg>
        <span>dana.mercer@northwaycoaching.com</span>
        <svg width="9" height="9" viewBox="0 0 10 10"><path d="M2 0l2 2.5-1 1.5c.7 1.3 1.7 2.3 3 3l1.5-1L10 8l-1.5 2C4.5 10 0 5.5 0 1.5z" fill="#2e3142"/></svg>
        <span>0400 123 456</span>
      </div>
    </div>

    <div class="detail-photo" role="img" aria-label="Black and white close-up of hands with a pen reviewing printed documents beside a laptop"></div>

    <div class="footer-rule"></div>
    <div class="footer-note">For details on other NWC services please visit&nbsp; www.northwaycoaching.com</div>
  </main>
</body>
</html>
```